Anzeigengestaltung für Steuerberatungsgesellschaft
Zielgruppe
Die KTR Steuerberatungsgesellschaft mbH zählt zu einer der führenden Steuerberatungsgesellschaften für mittelständische Unternehmen in Sachsen. Unabhängig, professionell und vertrauensvoll. Getreu unserem Leitbild 'Unternehmer beraten Unternehmer' werden Sie von einem konstanten Beratungsteam betreut, welches sich an den Standorten Görlitz und Dres-den um ALLE Ihre steuerlichen Fragen und Themen kümmert. Darüber hinaus verfügen unse-re Mitarbeiter über ein umfangreiches betriebswirtschaftliches Fachwissen und sind daher jederzeit in der Lage, Sie auch in angrenzenden Themen zu unterstützen.
Aufgabenstellung
Siehe Briefing (ppt)

```html
<!DOCTYPE html>
<html lang="de">
<head>
<meta charset="utf-8">
<title>KTR Steuerberatung – Stellenanzeige</title>
<link rel="stylesheet" href="https://fonts.googleapis.com/css2?family=Roboto+Condensed:wght@400;500;700&display=swap">
<style>
  :root {
    --sky-light: #b9d5ea;
    --sky-mid: #9fc3e1;
    --sky-deep: #8ab4d8;
    --navy: #1d2845;
    --brick: #9a3a31;
    --white: #ffffff;
    --badge-tint: rgba(255, 255, 255, 0.35);
    --photo-warm: #c9a58c;
    --photo-hair: #a7825f;
  }
  * { box-sizing: border-box; margin: 0; padding: 0; }
  html, body { width: 1200px; height: 628px; overflow: hidden; }
  body { font-family: "Roboto Condensed", "Arial Narrow", sans-serif; }

  .ad {
    position: relative;
    width: 1200px;
    height: 628px;
    overflow: hidden;
    background: radial-gradient(ellipse at 45% 45%, var(--sky-light) 0%, var(--sky-mid) 55%, var(--sky-deep) 100%);
    color: var(--navy);
  }

  .portrait {
    position: absolute;
    left: 760px;
    top: 60px;
    width: 440px;
    height: 568px;
    background:
      radial-gradient(ellipse at 30% 45%, var(--photo-warm) 0%, rgba(201,165,140,0.6) 30%, transparent 60%),
      linear-gradient(100deg, transparent 0%, rgba(167,130,95,0.55) 40%, rgba(167,130,95,0.35) 70%, transparent 100%);
    border-radius: 45% 10% 0 0;
    opacity: 0.85;
  }

  .headline {
    position: absolute;
    left: 40px;
    top: 76px;
    font-weight: 700;
    font-size: 82px;
    line-height: 86px;
    letter-spacing: 1.5px;
    text-transform: uppercase;
  }

  .locations {
    position: absolute;
    left: 46px;
    top: 255px;
    font-size: 21px;
    font-weight: 400;
    letter-spacing: 0.3px;
    text-transform: uppercase;
  }

  .position {
    position: absolute;
    left: 46px;
    top: 301px;
    padding-left: 14px;
    border-left: 13px solid var(--brick);
    font-size: 26px;
    line-height: 34px;
    font-weight: 400;
  }

  .bonus {
    position: absolute;
    left: 470px;
    top: 304px;
    width: 192px;
    height: 192px;
    border-radius: 50%;
    background: var(--navy);
    color: var(--white);
    display: flex;
    flex-direction: column;
    align-items: center;
    justify-content: center;
    transform: rotate(-8deg);
  }
  .bonus__amount { font-size: 44px; font-weight: 700; line-height: 1; }
  .bonus__label { font-size: 22px; font-weight: 500; margin-top: 6px; text-transform: uppercase; }

  .brand {
    position: absolute;
    left: 46px;
    top: 512px;
    display: flex;
    align-items: center;
    gap: 16px;
    font-size: 66px;
    line-height: 1;
    font-weight: 700;
    color: var(--navy);
    letter-spacing: 4px;
  }
  .brand__mark {
    width: 24px;
    height: 24px;
    background: var(--navy);
  }

  .partner-badge {
    position: absolute;
    left: 362px;
    top: 516px;
    width: 68px;
    height: 68px;
    border-radius: 50%;
    background: var(--badge-tint);
  }

  .hotline {
    position: absolute;
    left: 727px;
    top: 527px;
    width: 437px;
    height: 64px;
    border: 3px solid var(--white);
    border-radius: 14px;
    background: var(--brick);
    color: var(--white);
    display: flex;
    align-items: center;
    gap: 14px;
    padding-left: 22px;
    font-size: 22px;
    font-weight: 700;
    letter-spacing: 0.5px;
    box-shadow: 0 2px 6px rgba(0,0,0,0.15);
  }
  .hotline svg { width: 30px; height: 30px; flex: none; }
  .hotline__number { margin-left: 4px; }
</style>
</head>
<body>
<main class="ad">
  <div class="portrait" role="img" aria-label="Foto einer überraschten Frau im Profil, deren Haare im Wind wehen"></div>

  <h1 class="headline">Frischer Wind<br>für Ihre Karriere</h1>

  <p class="locations">Wir suchen für unsere Büros in Dresden/ Görlitz/ Home-Office</p>

  <p class="position">1x Steuerfachangestellter (m/w/d)<br>und Steuerfachwirt (m/w/d) mit<br>Kenntnissen LOHNSOFT PRO</p>

  <div class="bonus">
    <span class="bonus__amount">2.500 €</span>
    <span class="bonus__label">Wechselprämie</span>
  </div>

  <div class="brand">
    <span>KTR</span>
    <span class="brand__mark"></span>
  </div>

  <div class="partner-badge" aria-hidden="true"></div>

  <div class="hotline">
    <svg viewBox="0 0 24 24" aria-hidden="true">
      <path fill="#ffffff" d="M6.6 10.8c1.4 2.8 3.8 5.1 6.6 6.6l2.2-2.2c.3-.3.7-.4 1-.2 1.1.4 2.3.6 3.6.6.6 0 1 .4 1 1V20c0 .6-.4 1-1 1C10.6 21 3 13.4 3 4c0-.6.4-1 1-1h3.5c.6 0 1 .4 1 1 0 1.3.2 2.5.6 3.6.1.3 0 .7-.2 1l-2.3 2.2z"/>
    </svg>
    <span>JOBHOTLINE</span>
    <span class="hotline__number">+49 3581 44 120 50</span>
  </div>
</main>
</body>
</html>
```